Easter Competition Flyer to Healthcare Clients with a chance to win 1 of 2 luxury hampers

An A5 promotional flyer to send to our clients for an Easter competition with the chance to win some Easter Egg /Chocolate hampers. For every shift booked between 19th - 22nd April they will be entered into a draw with the chance to win 1 of 3 prizes available consisting of Easter Egg/Chocolate hampers (images attached)

Target Market(s)

Current and potential clients in the Healthcare Sector

Industry/Entity Type

Healthcare

Font styles to use
Decorative
Script

Colors

Designer to choose colors to be used in the design.

Requirements
Must have
• Company logo, Company colours, Branch contact details - To book call us now on Maidstone 01632 960418, Tonbridge 01632 960527, Ashford 01632 960639, Dartford 01632 960742 Website - www.carewaybookingsolutions.co.uk, Details of the competition (For every shift booked between 19th - 22nd April you will automatically be entered into our Easter prize draw for a chance to win 1 of 3 luxury Easter Hampers) - 3 available, pictures similar to prizes (images attached)
Nice to have
• Its a fun competitions so open to some fun Easter pictures of eggs and bunnies and other Easter related images
Should not have
• Too serious or corporate feel to it

```html
<!DOCTYPE html>
<html lang="en">
<head>
<meta charset="utf-8">
<title>Easter Competition Flyer</title>
<link href="https://fonts.googleapis.com/css2?family=Great+Vibes&family=Montserrat:wght@900&family=Oswald:wght@500&family=Open+Sans:wght@400;700;800&display=swap" rel="stylesheet">
<style>
  :root {
    --page-bg: #5a5a5a;
    --sky: #4fd3e8;
    --sky-light: #8fe6f2;
    --navy: #1450b4;
    --navy-dark: #0b3f94;
    --royal: #1966cc;
    --teal: #16d0b4;
    --teal-dark: #0fb39b;
    --egg: #b8743f;
    --white: #ffffff;
  }
  * { box-sizing: border-box; margin: 0; padding: 0; }
  html, body { width: 1200px; height: 1200px; overflow: hidden; }
  body {
    background: radial-gradient(circle at 50% 45%, #6b6b6b, #404040);
    font-family: "Open Sans", sans-serif;
    position: relative;
  }
  .flyer {
    position: absolute; left: 210px; top: 50px;
    width: 780px; height: 1100px; overflow: hidden;
    background: radial-gradient(circle at 50% 45%, var(--sky-light) 0%, var(--sky) 60%, #33bfd8 100%);
    box-shadow: 0 10px 40px rgba(0,0,0,.4);
  }
  .flyer > * { position: absolute; }
  .brand-box {
    left: 230px; top: 0; width: 320px; height: 140px;
    background: var(--white); border-radius: 0 0 14px 14px;
    display: flex; align-items: center; justify-content: center; gap: 12px;
  }
  .brand-dot { width: 18px; height: 18px; border-radius: 50%; background: var(--teal-dark); flex: none; }
  .brand-name { font-family: "Open Sans", sans-serif; font-weight: 700; font-size: 28px; color: var(--navy); white-space: nowrap; }
  .egg-art { left: 140px; top: 200px; width: 500px; height: 600px; }
  .shapes { left: 0; top: 0; width: 780px; height: 1100px; }
  .title-script {
    left: 0; width: 780px; top: 230px; text-align: center;
    font-family: "Great Vibes", cursive; font-size: 130px; line-height: 1; color: var(--teal);
  }
  .title-main {
    left: 0; width: 780px; top: 340px; text-align: center;
    font-family: "Montserrat", sans-serif; font-weight: 900; font-size: 80px; letter-spacing: 2px; color: var(--white);
  }
  .booking { left: 230px; top: 455px; width: 320px; text-align: center; color: var(--white); }
  .booking-head { font-family: "Oswald", sans-serif; font-weight: 500; font-size: 27px; margin-bottom: 10px; letter-spacing: .5px; }
  .branch-name { font-weight: 800; font-size: 21px; line-height: 1.15; }
  .branch-phone { font-size: 21px; line-height: 1.15; margin-bottom: 8px; letter-spacing: 1px; }
  .choc-egg { left: 20px; top: 610px; width: 190px; height: 180px; }
  .hamper { left: 572px; top: 640px; width: 190px; height: 180px; }
  .details { left: 40px; width: 700px; top: 840px; text-align: center; color: var(--white); }
  .details-head { font-weight: 800; font-size: 33px; color: var(--teal); margin-bottom: 6px; }
  .details-lead { font-weight: 800; font-size: 27px; line-height: 1.25; }
  .details-body { font-size: 19px; line-height: 1.35; }
  .details-prize { font-weight: 800; font-size: 27px; line-height: 1.25; }
  .more-info {
    left: 0; width: 780px; top: 995px; text-align: center;
    font-family: "Great Vibes", cursive; font-size: 48px; color: var(--teal);
  }
  .contacts {
    left: 0; width: 780px; top: 1055px; display: flex; justify-content: center; align-items: center; gap: 14px;
    color: var(--white); font-size: 17px;
  }
  .contact-item { display: flex; align-items: center; gap: 7px; }
  .contact-divider { width: 2px; height: 24px; background: var(--white); }
</style>
</head>
<body>
<main class="flyer">
  <svg class="egg-art" viewBox="0 0 500 600" role="img" aria-label="Large decorated chocolate Easter egg illustration">
    <ellipse cx="250" cy="300" rx="240" ry="290" fill="var(--egg)"/>
  </svg>

  <svg class="shapes" viewBox="0 0 780 1100" aria-hidden="true">
    <defs>
      <linearGradient id="panelGrad" x1="0" y1="0" x2="0" y2="1">
        <stop offset="0" stop-color="var(--navy)"/>
        <stop offset="1" stop-color="var(--royal)"/>
      </linearGradient>
    </defs>
    <polygon points="0,300 60,300 60,450 0,450 30,375" fill="var(--navy-dark)"/>
    <polygon points="780,300 720,300 720,450 780,450 750,375" fill="var(--navy-dark)"/>
    <rect x="40" y="240" width="700" height="190" fill="var(--navy)"/>
    <polygon points="40,430 60,450 60,430" fill="#0a2f70"/>
    <polygon points="740,430 720,450 720,430" fill="#0a2f70"/>
    <polygon points="220,430 560,430 560,760 390,715 220,760" fill="var(--teal)"/>
    <polygon points="220,430 560,430 560,445 220,445" fill="var(--teal-dark)"/>
    <path d="M0,790 L40,770 L80,800 L120,770 L160,800 L200,770 L240,800 L280,770 L320,800 L360,770 L400,800 L440,770 L480,800 L520,770 L560,800 L600,770 L640,800 L680,770 L720,800 L760,770 L780,785 L780,1100 L0,1100 Z" fill="url(#panelGrad)"/>
  </svg>

  <div class="brand-box">
    <span class="brand-dot"></span>
    <span class="brand-name">Careway Bookings</span>
  </div>

  <div class="title-script">Easter</div>
  <div class="title-main">COMPETITION</div>

  <div class="booking">
    <div class="booking-head">TO BOOK CALL US NOW ON</div>
    <div class="branch-name">Maidstone :</div>
    <div class="branch-phone">01632 960418</div>
    <div class="branch-name">Tonbridge :</div>
    <div class="branch-phone">01632 960527</div>
    <div class="branch-name">Ashford :</div>
    <div class="branch-phone">01632 960639</div>
    <div class="branch-name">Dartford :</div>
    <div class="branch-phone">01632 960742</div>
  </div>

  <svg class="choc-egg" viewBox="0 0 190 180" role="img" aria-label="Chocolate Easter eggs tied with a red ribbon bow">
    <ellipse cx="95" cy="90" rx="88" ry="84" fill="#6b3a1e"/>
  </svg>

  <svg class="hamper" viewBox="0 0 190 180" role="img" aria-label="Wicker hamper of foil-wrapped Easter eggs with a blue bow">
    <ellipse cx="95" cy="90" rx="90" ry="84" fill="#9a7fc2"/>
  </svg>

  <section class="details">
    <div class="details-head">Details of the competition</div>
    <div class="details-lead">For every shift booked between 19th - 22nd April</div>
    <div class="details-body">you will automatically be entered into our Easter prize draw for a chance to</div>
    <div class="details-prize">win 1 of 3 luxury Easter Hampers</div>
  </section>

  <div class="more-info">For more information</div>

  <div class="contacts">
    <span class="contact-item">
      <svg width="18" height="13" viewBox="0 0 18 13" aria-hidden="true"><rect x="0.5" y="0.5" width="17" height="12" fill="var(--teal)"/><polyline points="1,1 9,7 17,1" fill="none" stroke="var(--navy)" stroke-width="1.5"/></svg>
      info@carewaybookingsolutions.co.uk
    </span>
    <span class="contact-divider"></span>
    <span class="contact-item">
      <svg width="16" height="16" viewBox="0 0 16 16" aria-hidden="true"><circle cx="8" cy="8" r="7" fill="none" stroke="var(--teal)" stroke-width="1.5"/><ellipse cx="8" cy="8" rx="3" ry="7" fill="none" stroke="var(--teal)" stroke-width="1.2"/><line x1="1" y1="8" x2="15" y2="8" stroke="var(--teal)" stroke-width="1.2"/></svg>
      www.carewaybookingsolutions.co.uk
    </span>
  </div>
</main>
</body>
</html>
```